Business Cards & Stationary for Dental Practice Consulting Company
Brevik Practice Management & Consulting
Business Cards & Stationary for Dental Practice Consulting Company - Consulting
Professional
Renata Brevik
CEO/Executive Consultant
20591 Corwin Ln. Lakewood, CO 80226
renata@brevikpracticeconsulting.com

```html
<!DOCTYPE html>
<html lang="en">
<head>
<meta charset="UTF-8">
<title>Brevik Practice Management &amp; Consulting — Business Cards</title>
<link href="https://fonts.googleapis.com/css2?family=Open+Sans:wght@300;400;600&display=swap" rel="stylesheet">
<style>
  :root {
    --backdrop: #e9e6e1;
    --navy: #1f2b5c;
    --orange: #ea5a2e;
    --teal: #2ba69c;
    --ink-light: #e6e9f2;
    --card-w: 720px;
    --card-h: 411px;
  }
  * { margin: 0; padding: 0; box-sizing: border-box; }
  html, body {
    width: 1200px; height: 904px; overflow: hidden;
    background: var(--backdrop);
    font-family: "Open Sans", Arial, sans-serif;
  }
  .sheet { position: relative; width: 1200px; height: 904px; }
  .card {
    position: absolute; left: 240px;
    width: var(--card-w); height: var(--card-h);
    background: var(--navy);
    border-radius: 22px;
    box-shadow: 0 6px 18px rgba(0,0,0,0.18);
    overflow: hidden;
  }
  .card--front { top: 28px; }
  .card--back  { top: 465px; }

  /* front face */
  .brand-mark {
    position: absolute; left: 50%; top: 50%;
    transform: translate(-50%, -50%);
    display: flex; flex-direction: column; align-items: center; gap: 16px;
  }
  .brand-mark__dot {
    width: 46px; height: 46px; border-radius: 50%;
    background: var(--teal);
  }
  .brand-mark__name {
    color: var(--teal); font-weight: 400;
    font-size: 17px; letter-spacing: 0.5px; white-space: nowrap;
  }

  /* back face */
  .back-brand {
    position: absolute; left: 56px; top: 232px;
    display: flex; align-items: center; gap: 12px;
  }
  .back-brand__dot {
    width: 34px; height: 34px; border-radius: 50%;
    background: var(--teal); flex: none;
  }
  .back-brand__name {
    color: var(--teal); font-size: 15px; font-weight: 400;
    letter-spacing: 0.3px; line-height: 1.35;
  }
  .contact {
    position: absolute; left: 430px; top: 62px;
    color: var(--ink-light);
  }
  .contact__name {
    color: var(--orange); font-size: 21px; font-weight: 600; line-height: 1.2;
  }
  .contact__title {
    font-size: 15px; font-weight: 300; margin-bottom: 26px;
  }
  .contact__address {
    font-size: 14px; font-weight: 300; line-height: 1.45; margin-bottom: 14px;
  }
  .contact__list { list-style: none; }
  .contact__item {
    display: flex; align-items: center; gap: 12px;
    font-size: 14px; font-weight: 300; line-height: 1.6;
    white-space: nowrap;
  }
  .contact__icon { width: 13px; height: 13px; flex: none; fill: var(--teal); }
</style>
</head>
<body>
<main class="sheet">
  <section class="card card--front" aria-label="Card front">
    <div class="brand-mark">
      <span class="brand-mark__dot"></span>
      <span class="brand-mark__name">Brevik Practice Management &amp; Consulting</span>
    </div>
  </section>

  <section class="card card--back" aria-label="Card back">
    <div class="back-brand">
      <span class="back-brand__dot"></span>
      <span class="back-brand__name">Brevik Practice Management<br>&amp; Consulting</span>
    </div>

    <div class="contact">
      <p class="contact__name">Renata Brevik</p>
      <p class="contact__title">CEO/Executive Consultant</p>
      <p class="contact__address">20591 Corwin Ln.<br>Lakewood, CO 80226</p>
      <ul class="contact__list">
        <li class="contact__item">
          <svg class="contact__icon" viewBox="0 0 16 16"><path d="M4 1l3 3-2 2c1 2 3 4 5 5l2-2 3 3-2 3C7 15 1 9 1 3z"/></svg>713-555-0142
        </li>
        <li class="contact__item">
          <svg class="contact__icon" viewBox="0 0 16 16"><rect x="2" y="5" width="12" height="9" rx="1"/><rect x="4" y="1" width="8" height="4"/></svg>713-555-0187
        </li>
        <li class="contact__item">
          <svg class="contact__icon" viewBox="0 0 16 16"><rect x="4" y="1" width="8" height="14" rx="1.5"/></svg>832-555-0163
        </li>
        <li class="contact__item">
          <svg class="contact__icon" viewBox="0 0 16 16"><path d="M1 3h14v10H1z M1 3l7 6 7-6" fill="none" stroke="#2ba69c" stroke-width="1.6"/></svg>renata@brevikpracticeconsulting.com
        </li>
      </ul>
    </div>
  </section>
</main>
</body>
</html>
```